Essential oil label for bottles

Looking to modify our current logo and label design. It looks too simple. I will attach images of our competitors to use as examples. Our company name is Velnora. We have 2 different bottles. Clear and amber color. Going forward, we will be using only the amber bottle. The other 2 images are the biggest sellers brands. We want to make some adjustments to ours.

Target Market(s)

Brindex sales

Industry/Entity Type

Essential oil, perfume

Colors

Designer to choose only greyscale colors for use in the design.

Requirements
Nice to have
• A slight change to fonts and logo design. Maybe change the font and design of the word "Velnora" in our logo. Maybe add something to the label to make it stand out more but still keeping it clean and modern
Should not have
• No colors, besides, black, grays, whites, and off white.

```html
<!DOCTYPE html>
<html lang="en">
<head>
<meta charset="UTF-8">
<title>Velnora — White Tea Fragrance Oil Label</title>
<link rel="stylesheet" href="https://fonts.googleapis.com/css2?family=Montserrat:wght@300;400&family=Open+Sans:wght@700&display=swap">
<style>
  :root {
    --canvas-bg: #efefef;
    --label-top: #48505a;
    --label-bottom: #6a727c;
    --label-ink-light: #ececec;
    --label-ink-dark: #2e3339;
    --rule-light: #8a929c;
    --rule-dark: #3a4047;
  }
  * { margin: 0; padding: 0; box-sizing: border-box; }
  html, body {
    width: 1200px;
    height: 900px;
    overflow: hidden;
    background: var(--canvas-bg);
  }
  .canvas {
    position: relative;
    width: 1200px;
    height: 900px;
  }
  .label {
    position: absolute;
    left: 291px;
    top: 60px;
    width: 618px;
    height: 780px;
    background: var(--label-top);
    overflow: hidden;
  }
  .brand {
    position: absolute;
    left: 77px;
    top: 58px;
    display: flex;
    align-items: center;
    gap: 22px;
  }
  .brand-dot {
    width: 40px;
    height: 40px;
    border-radius: 50%;
    border: 3px solid var(--label-ink-light);
  }
  .brand-name {
    font-family: "Montserrat", sans-serif;
    font-weight: 300;
    font-size: 56px;
    letter-spacing: 6px;
    color: var(--label-ink-light);
    line-height: 1;
  }
  .product-name {
    position: absolute;
    left: 50px;
    top: 310px;
    font-family: "Open Sans", sans-serif;
    font-weight: 700;
    font-size: 82px;
    letter-spacing: 5px;
    color: var(--label-ink-light);
    line-height: 1;
    white-space: nowrap;
  }
  .product-rule {
    position: absolute;
    left: 0;
    top: 401px;
    width: 557px;
    height: 3px;
    background: var(--rule-light);
  }
  .details {
    position: absolute;
    left: 0;
    top: 535px;
    width: 100%;
    height: 245px;
    background: var(--label-bottom);
    font-family: "Montserrat", sans-serif;
    font-weight: 400;
    color: var(--label-ink-dark);
  }
  .details-type {
    position: absolute;
    left: 38px;
    top: 32px;
    font-size: 24px;
    letter-spacing: 0.5px;
  }
  .details-rule {
    position: absolute;
    left: 38px;
    top: 67px;
    width: 478px;
    height: 1.5px;
    background: var(--rule-dark);
  }
  .details-notes {
    position: absolute;
    left: 38px;
    top: 76px;
    display: flex;
    font-size: 24px;
    letter-spacing: 0.3px;
  }
  .note + .note {
    border-left: 1.5px solid var(--label-ink-dark);
    margin-left: 6px;
    padding-left: 6px;
  }
  .details-volume {
    position: absolute;
    left: 38px;
    top: 190px;
    font-size: 22px;
  }
</style>
</head>
<body>
  <main class="canvas">
    <section class="label">
      <div class="brand">
        <span class="brand-dot"></span>
        <span class="brand-name">VELNORA</span>
      </div>

      <h1 class="product-name">WHITE TEA</h1>
      <div class="product-rule"></div>

      <div class="details">
        <p class="details-type">FRAGANCE OIL</p>
        <div class="details-rule"></div>
        <p class="details-notes">
          <span class="note">WHITE TEA</span>
          <span class="note">ORANGE</span>
          <span class="note">PALO SANTO</span>
        </p>
        <p class="details-volume">200ML</p>
      </div>
    </section>
  </main>
</body>
</html>
```